Jazz: Journey Through the Harlem Renaissance and the Black Arts Movement

Corvel Tavern invites you on a musical Journey Through the Harlem Renaissance and the Black Arts Movement!
Join us for an afternoon of Jazz on Sunday, February 27, 2022 from 3pm – 5pm.
Local jazz artists will thrill you with the music of legendary Harlem Renaissance artists such as Royce Tamberlin and Odessa Crane and famed Black Arts Movement stylings reminiscent of Vernon Askew and Lydia Farrow.
There will be games, prizes and opportunities to support arts programs at local schools.

```html
<!DOCTYPE html>
<html lang="en">
<head>
<meta charset="utf-8">
<title>Afternoon of Jazz – Corvel Tavern</title>
<link rel="stylesheet" href="https://fonts.googleapis.com/css2?family=Poppins:wght@400;500;600;700;800&display=swap">
<style>
  :root {
    --canvas: #efefef;
    --ink: #141414;
    --night: #1b1b1b;
    --paper: #ffffff;
    --gold: #d8a928;
    --smoke: #2e2e2e;
  }
  * { margin: 0; padding: 0; box-sizing: border-box; }
  html, body {
    width: 1200px; height: 3308px; overflow: hidden;
    background: var(--canvas);
    font-family: "Poppins", sans-serif;
  }
  .poster {
    position: absolute; left: 50px; top: 774px;
    width: 1100px; height: 1760px;
    background: var(--paper); overflow: hidden;
    box-shadow: 0 6px 24px rgba(0,0,0,.12);
  }
  .poster__backdrop { position: absolute; inset: 0; }
  .poster__art { position: absolute; left: 0; top: 90px; width: 440px; height: 1560px; }

  .content {
    position: absolute; left: 440px; top: 60px; width: 640px;
    display: flex; flex-direction: column; align-items: center; text-align: center;
  }
  .brand { display: flex; flex-direction: column; align-items: center; gap: 10px; }
  .brand__mark { width: 84px; height: 84px; border-radius: 50%; border: 4px solid var(--gold); }
  .brand__name { font-weight: 600; font-size: 22px; color: var(--gold); letter-spacing: 3px; text-transform: uppercase; }

  .invite { margin-top: 50px; font-weight: 700; font-size: 28px; line-height: 1.25; color: var(--ink); text-transform: uppercase; }
  .headline { margin-top: 18px; font-weight: 800; font-size: 58px; line-height: 1.08; color: var(--gold); text-transform: uppercase; }

  .join { margin-top: 300px; font-weight: 700; font-size: 50px; line-height: 1.1; color: var(--gold); text-transform: uppercase; }
  .afternoon { font-weight: 400; font-size: 54px; line-height: 1.25; color: var(--paper); }

  .when { margin-top: 28px; width: 600px; color: var(--paper); text-align: left; }
  .when__row { display: flex; align-items: center; }
  .when__day { background: var(--gold); color: var(--ink); font-weight: 700; font-size: 38px; line-height: 1.3; padding: 0 20px; text-transform: uppercase; }
  .when__from { margin-left: 60px; font-weight: 700; font-size: 42px; text-transform: uppercase; }
  .when__date { margin-top: 14px; font-weight: 700; font-size: 36px; line-height: 1.2; text-transform: uppercase; white-space: nowrap; }
  .when__date sup { font-size: 20px; }
  .when__date .divider { display: inline-block; width: 3px; height: 38px; background: var(--paper); margin: 0 18px; vertical-align: -6px; }

  .details { margin-top: 34px; font-size: 21px; line-height: 1.7; color: var(--paper); }
  .details .lead { font-size: 29px; display: block; line-height: 1.4; margin-bottom: 6px; }
  .details .name { background: var(--paper); color: var(--ink); font-weight: 600; padding: 0 6px; white-space: nowrap; }
  .details .accent { color: var(--gold); }

  .extras {
    position: absolute; left: 440px; top: 1650px; width: 640px;
    background: var(--gold); color: var(--ink);
    font-weight: 700; font-size: 17px; line-height: 1.4; text-align: center; padding: 12px 10px;
    text-transform: uppercase;
  }
</style>
</head>
<body>
  <main class="poster">
    <svg class="poster__backdrop" viewBox="0 0 1100 1760" preserveAspectRatio="none" aria-hidden="true">
      <path d="M0 0 H400 C360 300 440 760 700 830 C880 870 1000 860 1100 890 V1760 H0 Z" fill="var(--night)"/>
      <path d="M620 830 C800 880 960 870 1100 910" fill="none" stroke="#ffffff" stroke-width="9"/>
      <path d="M600 870 C800 920 960 910 1100 950" fill="none" stroke="var(--smoke)" stroke-width="14"/>
    </svg>

    <svg class="poster__art" viewBox="0 0 440 1560" preserveAspectRatio="none" role="img" aria-label="Silhouette illustration of a jazz saxophonist in a gold hat playing a gold saxophone">
      <defs>
        <linearGradient id="artTone" x1="0" y1="0" x2="1" y2="1">
          <stop offset="0" stop-color="#0c0c0c"/>
          <stop offset=".55" stop-color="#262626"/>
          <stop offset="1" stop-color="#8a6a1c"/>
        </linearGradient>
      </defs>
      <path d="M100 0 C220 -10 300 120 320 300 C350 520 430 760 420 1080 C400 1320 340 1480 260 1560 H0 V60 Z" fill="url(#artTone)"/>
    </svg>

    <section class="content">
      <div class="brand">
        <span class="brand__mark"></span>
        <span class="brand__name">Corvel Tavern</span>
      </div>

      <p class="invite">Corvel Tavern invites you<br>on a musical journey through</p>
      <h1 class="headline">The Harlem<br>Renaissance<br>&amp;<br>The Black Arts<br>Movement!</h1>

      <p class="join">Join us for an</p>
      <p class="afternoon">Afternoon of Jazz</p>

      <div class="when">
        <div class="when__row">
          <span class="when__day">On Sunday</span>
          <span class="when__from">From</span>
        </div>
        <div class="when__date">27<sup>th</sup> February, 2022<span class="divider"></span>3pm - 5pm</div>
      </div>

      <p class="details">
        <span class="lead">Local jazz artists will thrill you with the music of</span>
        <span class="accent">legendary Harlem Renaissance artists such as</span> <span class="name">Royce Tamberlin</span> and <span class="name">Odessa Crane</span><br>
        <span class="accent">famed Black Arts Movement stylings reminiscent of</span> <span class="name">Vernon Askew</span> and <span class="name">Lydia Farrow</span>.
      </p>
    </section>

    <p class="extras">There will be games, prizes and opportunities to support arts programs at local schools.</p>
  </main>
</body>
</html>
```